Contemporary Business card for Event Manager

Needed for my startup events company in Melbourne. Events I manage will be based within the fashion industry, sporting events, product launches etc. Not weddings or small dinner parties. Therfore I am after something professional and aimed at high end corporate market; but with the added emphasis on not being too conservative or boring. I am happy with a pop of colour e.g. yellow or copper foil.

Target Market(s)

fashion industry, design industry, high end sporting events e.g. Polo, Grand Prix, corporate clients,

Industry/Entity Type

Fashion

Contact Information for Business Card

side 1
Rosa Whitfield (can be upper or lower case, have a feature full stop between first and surname, or at the end of the nameetc) I am open to ideas. I would also be fine with my initials or name as a logo on the front (if this is the case my full name would need to go on the second side of the card.
2nd side:
Mobile: +61 455 718 263
email: rosa.whitfield@kestrelpost.com.au

on one side of the card:
event management | brand activation | Advisory Services

Font styles to use
Serif
Sans Serif

Requirements
Must have
• side 2 must have
• mobile number
• email address
• event management | brand activation | Advisory Services
• ** my full name (Rosa Whitfield) must be on the card somewhere)
Nice to have
• 1st side
• I see the card stock being either a dark grey, light grey, natural white or black (all matt colours on unprocessed card). I see the writing being copper foil, or foil white or foil black.
• To give you a feel for me, think: contemporary, minimalist, I love line drawings, concrete, white with grey vein marble, copper, white, grey, black...yes I do like colour....yellow (but pops of colour) ;) I would like the card to look designer but 'on trend' as I deal with a lot of design and fashion clients....styles - think the sophistication and simplicity of Lisoret or urban contemporary.
• some examples of what I like. Although please don't leet this limit you...I really am happy to have something a little more urban or design focused like a line drawing of an object, person too or a photo image too.
• https://www.pinvaultly.com/pin/837205164932850174/
• https://www.pinvaultly.com/pin/926318450173648205/
• https://www.pinvaultly.com/pin/318604927551203847/
• https://www.pinvaultly.com/pin/50938162477420916/
• https://www.pinvaultly.com/pin/41276039158862793/
• https://www.pinvaultly.com/pin/63098817524506139/
• https://www.pinvaultly.com/pin/704129583366208154/
• https://www.pinvaultly.com/pin/582046317729851460/
• https://www.pinvaultly.com/pin/467318205542097831/
Should not have
• should not look commercial or have cartoonish looking logos. However happy with a simple line drawing or logo with initials etc.

```html
<!DOCTYPE html>
<html lang="en">
<head>
<meta charset="utf-8">
<title>Rosa Whitfield — Business Card</title>
<link rel="stylesheet" href="https://fonts.googleapis.com/css2?family=Mulish:wght@700&family=Questrial&display=swap">
<style>
  :root {
    --backdrop: #e6e4e1;
    --card-stock: #202020;
    --ink-white: #f4f4f4;
    --ink-blind: #151515;
    --card-shadow: rgba(0, 0, 0, 0.28);
  }
  * { box-sizing: border-box; margin: 0; padding: 0; }
  html, body {
    width: 1200px;
    height: 1000px;
    overflow: hidden;
    background: var(--backdrop);
  }
  .canvas {
    position: relative;
    width: 1200px;
    height: 1000px;
  }
  .card {
    position: absolute;
    left: 265px;
    width: 666px;
    height: 397px;
    background: var(--card-stock);
    box-shadow: 0 6px 14px var(--card-shadow);
    color: var(--ink-white);
    text-align: center;
    font-family: "Questrial", "Century Gothic", sans-serif;
  }
  .card--contact { top: 73px; }
  .card--monogram { top: 532px; }

  .contact__name {
    position: absolute;
    top: 111px;
    left: 0;
    right: 0;
    height: 28px;
    line-height: 28px;
    font-family: "Mulish", "Century Gothic", sans-serif;
    font-weight: 700;
    font-size: 23px;
    letter-spacing: 0.2px;
  }
  .contact__line {
    position: absolute;
    left: 0;
    right: 0;
    height: 20px;
    line-height: 20px;
    font-size: 17px;
    letter-spacing: 0.2px;
  }
  .contact__icon {
    position: absolute;
    left: 326px;
    width: 14px;
    height: 12px;
  }
  .contact__icon--phone { top: 156px; }
  .contact__icon--mail { top: 197px; }
  .contact__line--phone { top: 170px; }
  .contact__line--mail { top: 209px; }
  .contact__services {
    position: absolute;
    top: 263px;
    left: 0;
    right: 0;
    height: 20px;
    line-height: 20px;
    font-size: 18px;
    letter-spacing: 0.3px;
  }
  .contact__services .divider { padding: 0 8px; }

  .monogram__name {
    position: absolute;
    top: 92px;
    left: 0;
    right: 0;
    font-family: "Questrial", "Century Gothic", sans-serif;
    font-size: 84px;
    line-height: 1.05;
    letter-spacing: 1px;
    color: var(--ink-blind);
  }
</style>
</head>
<body>
<main class="canvas">
  <section class="card card--contact">
    <h1 class="contact__name">Rosa Whitfield</h1>

    <svg class="contact__icon contact__icon--phone" viewBox="0 0 14 12" aria-hidden="true">
      <path d="M3.2 10.5 C2.4 7.2 4.2 3.4 7.6 1.6 L9.2 1 L10.4 3.1 L8.9 3.9 C6.9 5 5.7 7.3 6 9.5 L4.6 10.4 Z" fill="var(--ink-white)"/>
    </svg>
    <p class="contact__line contact__line--phone">+61 455 718 263</p>

    <svg class="contact__icon contact__icon--mail" viewBox="0 0 14 12" aria-hidden="true">
      <rect x="1" y="1.5" width="12" height="9" fill="var(--ink-white)"/>
      <path d="M1 1.5 L7 6.5 L13 1.5" fill="none" stroke="var(--card-stock)" stroke-width="1"/>
    </svg>
    <p class="contact__line contact__line--mail">rosa.whitfield@kestrelpost.com.au</p>

    <p class="contact__services">Event Management<span class="divider">|</span>Brand Activation<span class="divider">|</span>Advisory Services</p>
  </section>

  <section class="card card--monogram">
    <p class="monogram__name">Rosa<br>Whitfield</p>
  </section>
</main>
</body>
</html>
```